Tobias Wrenfield - Cinematographer

NEED:
I'm looking for a sleek, professional, modern business card that will give give the recipient the impression that they can trust their production will go smoothly by hiring me. I will bring creativity and knowledge to their shoot, so that we can create powerful images.
I am looking for a card with a strong style and design ethos that could be expanded to a website and a full visual/graphic/design entity for me.
ABOUT ME:
I am a mid-twenties cinematographer, I work on music video, narrative short, commercial, and corporate projects. I blend the science and artistry of cameras and filmmaking to tell a story. I'm an artist, a technician, and a manager.
DESIGN:
I like sleek, simple design. Black, dark grays, white, dark navy, steel blues, I love cyan, but also cyan and red. I am not a fan of earthy tones. I generally prefer modern, san-serif fonts over serifs. My old logo was based on an aperture, a multi-blade device at the back of a lens that controls how much light passes through, but I made it with so many colors, that it doesn't necessarily lend itself to a specific color-scheme or design ethos. I liked that the aperture design provided a sense of the technical requirements of my job. I'm a fan of matte business cards, but am open to plenty of specialty print processes to make an outstanding card.
ATTACHED FILES:
My Old Rainbox Aperture Logo, plus a few designs I've tried playing around with, but am not tied to. I AM OPEN TO NEW DESIGNS, DO NOT FEEL TIED TO THIS.
**I've pulled my old logo down from the attached files, and instead attached other business cards I like, so as not to mislead you where I would like to go.
INFO:
Name: Tobias Wrenfield
Job: Cinematographer
Email: tkwrenfield@quillbox.example
Phone: 503.618.2907
Website: tobiaswrenfield.example
Updates
I'm adding some images of other cards that I like, and removing my old logo, since I'm looking for something new, and don't want that old logo to push anyone a certain direction.

```html
<!DOCTYPE html>
<html lang="en">
<head>
<meta charset="utf-8">
<title>Tobias Wrenfield — Cinematographer Business Card</title>
<link rel="stylesheet" href="https://fonts.googleapis.com/css2?family=Archivo+Black&family=Arimo:wght@400&display=swap">
<style>
  :root {
    --backdrop: #d9d9d9;
    --card-white: #ffffff;
    --card-black: #050505;
    --ink: #141414;
    --mark-faint: #f1f1f1;
    --mark-dark: #4a4a4a;
    --url-light: #f2f2f2;
    --accent-cyan: #29a9e0;
  }
  * { margin: 0; padding: 0; box-sizing: border-box; }
  html, body {
    width: 1200px;
    height: 926px;
    overflow: hidden;
    background: var(--backdrop);
  }
  .canvas {
    position: relative;
    width: 1200px;
    height: 926px;
  }
  .card {
    position: absolute;
    left: 260px;
    width: 680px;
    height: 388px;
    overflow: hidden;
    box-shadow: 0 6px 18px rgba(0,0,0,0.18);
  }
  .card--back {
    top: 55px;
    background: var(--card-black);
  }
  .card--front {
    top: 483px;
    background: var(--card-white);
  }

  /* Back side */
  .back-mark {
    position: absolute;
    left: 0; right: 0;
    top: 172px;
    text-align: center;
    font-family: "Archivo Black", sans-serif;
    font-size: 46px;
    letter-spacing: -1px;
    color: var(--mark-dark);
  }
  .back-url {
    position: absolute;
    left: 0; right: 0;
    top: 142px;
    text-align: center;
    font-family: "Arimo", sans-serif;
    font-size: 15px;
    letter-spacing: 5px;
    color: var(--url-light);
  }

  /* Front side */
  .front-mark {
    position: absolute;
    left: 40px;
    bottom: 40px;
    font-family: "Archivo Black", sans-serif;
    font-size: 92px;
    line-height: 0.92;
    letter-spacing: -3px;
    color: var(--mark-faint);
  }
  .identity {
    position: absolute;
    right: 42px;
    top: 40px;
    text-align: right;
  }
  .identity__name {
    font-family: "Archivo Black", sans-serif;
    font-size: 30px;
    letter-spacing: 0.5px;
    color: var(--ink);
    line-height: 1.05;
  }
  .identity__role {
    font-family: "Arimo", sans-serif;
    font-size: 17px;
    color: var(--ink);
    letter-spacing: 0.3px;
  }
  .contact {
    position: absolute;
    right: 36px;
    bottom: 40px;
    list-style: none;
  }
  .contact__item {
    display: flex;
    justify-content: flex-end;
    align-items: center;
    gap: 14px;
    font-family: "Arimo", sans-serif;
    font-size: 19px;
    color: var(--ink);
    line-height: 1.55;
  }
  .contact__icon {
    width: 16px;
    height: 16px;
    flex: none;
  }
</style>
</head>
<body>
<main class="canvas">

  <section class="card card--back" aria-label="Card back">
    <p class="back-url">www.tobiaswrenfield.example</p>
    <p class="back-mark">Tobias Wrenfield</p>
  </section>

  <section class="card card--front" aria-label="Card front">
    <p class="front-mark" aria-hidden="true">Tobias<br>Wrenfield</p>

    <header class="identity">
      <h1 class="identity__name">TOBIAS WRENFIELD</h1>
      <p class="identity__role">cinematographer</p>
    </header>

    <ul class="contact">
      <li class="contact__item">
        <span>tkwrenfield@quillbox.example</span>
        <svg class="contact__icon" viewBox="0 0 16 16" aria-hidden="true">
          <rect x="1" y="3" width="14" height="10" fill="var(--accent-cyan)"/>
          <polyline points="1,3.5 8,9 15,3.5" fill="none" stroke="#fff" stroke-width="1.3"/>
        </svg>
      </li>
      <li class="contact__item">
        <span>503.618.2907</span>
        <svg class="contact__icon" viewBox="0 0 16 16" aria-hidden="true">
          <rect x="3.5" y="0.5" width="9" height="15" rx="1.5" fill="var(--accent-cyan)"/>
          <rect x="5" y="2.5" width="6" height="9" fill="#fff"/>
          <circle cx="8" cy="13.5" r="0.9" fill="#fff"/>
        </svg>
      </li>
      <li class="contact__item">
        <span>www.tobiaswrenfield.example</span>
        <svg class="contact__icon" viewBox="0 0 16 16" aria-hidden="true">
          <circle cx="8" cy="8" r="7" fill="var(--accent-cyan)"/>
          <g fill="none" stroke="#fff" stroke-width="1">
            <ellipse cx="8" cy="8" rx="3" ry="7"/>
            <line x1="1" y1="8" x2="15" y2="8"/>
            <line x1="8" y1="1" x2="8" y2="15"/>
          </g>
        </svg>
      </li>
    </ul>
  </section>

</main>
</body>
</html>
```